Cozy Sprouts Business Cards

I need a business card for my new Company called Cozy Sprouts. We create handmade baby moccasins, headbands, t-shirts and more. I want some that will appeal to parents, and to go with the colors of my logo that I have attached. feel free to be creative. I would like my logo placed somewhere on the card.

Industry/Entity Type

Retail

Contact Information for Business Card

Cozy Sprouts
24816 Maplecrest D #5172
Irvine Ca 92738
Rosalind Vantrey Ceo
Info@Cozy-Sprouts.com
www.Cozy-Sprouts.com
Phone 9495817320

Requirements
Nice to have
• Logo included

```html
<!DOCTYPE html>
<html lang="en">
<head>
<meta charset="utf-8">
<title>Cozy Sprouts – Business Card</title>
<link rel="stylesheet" href="https://fonts.googleapis.com/css2?family=Open+Sans:wght@400&display=swap">
<style>
  :root {
    --stage: #e6e4e1;
    --card-dark: #141414;
    --card-mid: #2a2a2a;
    --band: #8e8e8e;
    --band-dark: #5c5c5c;
    --brand-text: #1b1b1b;
    --accent: #f07f4f;
    --text-light: #f2f2f2;
    --icon-ring: #e9e9e9;
    --icon-core: #555555;
  }
  * { box-sizing: border-box; margin: 0; padding: 0; }
  html, body {
    width: 1200px;
    height: 873px;
    overflow: hidden;
    background: var(--stage);
    font-family: "Open Sans", sans-serif;
  }
  .business-card {
    position: absolute;
    left: 100px;
    top: 145px;
    width: 1000px;
    height: 583px;
    overflow: hidden;
    background: linear-gradient(160deg, var(--card-mid) 0%, var(--card-dark) 45%, #1d1d1d 100%);
    box-shadow: 0 10px 30px rgba(0,0,0,.25);
  }
  .card-texture {
    position: absolute;
    right: 0;
    top: 0;
    width: 400px;
    height: 583px;
    background: linear-gradient(200deg, #4a4a4a 0%, #2c2c2c 40%, rgba(30,30,30,0) 100%);
  }
  .name-band {
    position: absolute;
    left: 50px;
    top: 144px;
    width: 420px;
    height: 62px;
    background: linear-gradient(90deg, var(--band) 0%, var(--band-dark) 100%);
  }
  .brand-name {
    position: absolute;
    left: 56px;
    top: 140px;
    font-size: 45px;
    line-height: 62px;
    color: var(--brand-text);
    letter-spacing: 1px;
  }
  .brand-square {
    position: absolute;
    left: 490px;
    top: 90px;
    width: 150px;
    height: 150px;
    border-radius: 18px;
    background: var(--accent);
  }
  .address {
    position: absolute;
    left: 56px;
    top: 222px;
    font-size: 29px;
    line-height: 32px;
    color: var(--text-light);
    letter-spacing: 1px;
  }
  .contact-row {
    position: absolute;
    left: 56px;
    display: flex;
    align-items: center;
    gap: 22px;
    color: var(--text-light);
  }
  .contact-row svg { width: 64px; height: 64px; flex: none; }
  .contact-row--person { top: 298px; font-size: 28px; }
  .contact-row--web { top: 380px; font-size: 23px; line-height: 29px; }
  .contact-row--phone { top: 463px; font-size: 23px; }
</style>
</head>
<body>
  <main class="business-card">
    <div class="card-texture" role="img" aria-label="Large faint decorative brand pattern of grey tiles"></div>

    <div class="name-band"></div>
    <h1 class="brand-name">Cozy Sprouts</h1>
    <div class="brand-square"></div>

    <p class="address">24816 Maplecrest D #5172<br>Irvine Ca 92738</p>

    <div class="contact-row contact-row--person">
      <svg viewBox="0 0 64 64" aria-hidden="true">
        <circle cx="32" cy="32" r="28" fill="none" stroke="var(--icon-ring)" stroke-width="6"/>
        <circle cx="32" cy="32" r="20" fill="var(--icon-core)"/>
        <circle cx="32" cy="27" r="6" fill="var(--icon-ring)"/>
        <path d="M20 42 q12 -14 24 0 z" fill="var(--icon-ring)"/>
      </svg>
      <span>Rosalind Vantrey Ceo</span>
    </div>

    <div class="contact-row contact-row--web">
      <svg viewBox="0 0 64 64" aria-hidden="true">
        <circle cx="32" cy="32" r="28" fill="none" stroke="var(--icon-ring)" stroke-width="6"/>
        <circle cx="32" cy="32" r="20" fill="var(--icon-core)"/>
        <rect x="21" y="23" width="22" height="15" rx="2" fill="var(--icon-ring)"/>
        <rect x="28" y="39" width="8" height="4" fill="var(--icon-ring)"/>
      </svg>
      <span>Info@Cozy-Sprouts.com<br>www.Cozy-Sprouts.com</span>
    </div>

    <div class="contact-row contact-row--phone">
      <svg viewBox="0 0 64 64" aria-hidden="true">
        <circle cx="32" cy="32" r="28" fill="none" stroke="var(--icon-ring)" stroke-width="6"/>
        <circle cx="32" cy="32" r="20" fill="var(--icon-core)"/>
        <rect x="22" y="24" width="20" height="16" rx="3" fill="var(--icon-ring)"/>
      </svg>
      <span>9495817320</span>
    </div>
  </main>
</body>
</html>
```